Need web design for our e-assessment company

We need a web design for our e-assessment company called Tavelo. We develop modern, web-based software for supporting the testing and examination process. The application is delivered as a SaaS solution.

The application helps our customers save time and money.

The design should communicate the following:

- Modern
- Innovation
- Security
- Performance

Attached you can find a screenshot of our application as well as some thoughts on the website.

We would like a front page as well as 1 sub page.

And lastly, one more website we draw inspiration from (on top of the ones mentioned in the attached document): http://www.plonkavery.example/
Updates

Dear all,

I have updated the description with 1 more example of websites we like as well as added that we would like a front page and a sub page.

Thanks in advance.

Best regards,

Torlak

Target Market(s)

Our target groups are higher education and awarding organisations. Decision makers are mostly men age 45+.

Industry/Entity Type

It Company

Requirements
Must have
• 1 front page and 1 sub page

```html
<!DOCTYPE html>
<html lang="en">
<head>
<meta charset="utf-8">
<title>Tavelo – e-Assessment, Simplified</title>
<link rel="stylesheet" href="https://fonts.googleapis.com/css2?family=Questrial&family=Arimo:wght@400;700&family=Kalam:wght@400;700&display=swap">
<style>
:root{
  --orange:#f26c21;
  --cyan:#1eaee8;
  --ink:#3f3f3f;
  --text:#6a6a6a;
  --muted:#9a9a9a;
  --white:#ffffff;
  --band:#d9d9d9;
  --band-dark:#d2d2d2;
  --soft:#ebebeb;
  --partner:#e6e6e6;
  --field:#d6d6d6;
  --icon:#5b5b5b;
  --rule:#c9c9c9;
}
*{box-sizing:border-box;margin:0;padding:0}
html,body{width:1200px;height:3440px;overflow:hidden}
body{background:var(--white);font-family:"Arimo",Arial,sans-serif;color:var(--text);position:relative}
.head{font-family:"Questrial",Arial,sans-serif}
.script{font-family:"Kalam",cursive}
section,header,footer{position:absolute;left:0;width:1200px}
.abs{position:absolute}

/* nav */
.site-nav{top:0;height:74px;background:var(--white)}
.brand{left:160px;top:20px;display:flex;align-items:center;gap:10px}
.brand-mark{width:34px;height:34px;border-radius:8px;background:var(--orange)}
.brand-name{font-family:"Questrial",sans-serif;font-size:30px;color:#555}
.nav-links{right:155px;top:28px;display:flex;gap:46px;list-style:none}
.nav-links li{font-size:13px;font-weight:700;color:#333;letter-spacing:.3px}

/* hero */
.hero{top:74px;height:558px;background:radial-gradient(ellipse at 50% 40%,#f6f6f6 0%,#e2e2e2 70%,#d8d8d8 100%)}
.promise{left:159px;display:flex;align-items:center;gap:16px}
.promise-text{font-size:22px;color:var(--orange);font-family:"Questrial",sans-serif}
.tagline{left:540px;top:72px;width:500px;text-align:right;white-space:nowrap;font-size:40px;line-height:56px;font-weight:700;color:var(--orange)}
.btn{display:flex;align-items:center;justify-content:center;color:var(--white);font-family:"Questrial",sans-serif;white-space:nowrap}
.btn-try{left:699px;top:155px;width:216px;height:37px;background:var(--cyan);font-size:22px}
.hero-photo{left:480px;top:200px;width:676px;height:358px;background:linear-gradient(160deg,#e9e9e9 0%,#cfcfcf 55%,#b8b8b8 100%);border-radius:4px 4px 0 0}
.hero-arrow{top:248px}

/* signup */
.signup{top:632px;height:138px;background:var(--band)}
.signup-title{left:155px;top:46px;font-size:34px;color:#555}
.btn-signup{left:561px;top:44px;width:231px;height:45px;background:var(--orange);font-size:22px}
.social{right:155px;top:54px;display:flex;gap:26px;font-size:18px;color:#8a8a8a;font-family:"Questrial",sans-serif}

/* how */
.how{top:770px;height:428px}
h2{font-family:"Questrial",sans-serif;font-weight:400;color:var(--ink)}
.how h2{position:absolute;left:155px;top:88px;font-size:34px}
.how-copy{left:155px;top:150px;width:500px;font-size:13px;line-height:18px}
.how-copy p+p{margin-top:18px}
.watch{left:155px;top:320px;font-size:26px;color:var(--orange)}
.video{left:701px;top:96px;width:339px;height:248px;background:linear-gradient(#ededed,#dcdcdc);border:1px solid #cfcfcf}

/* features */
.features{top:1198px;height:490px;background:var(--soft)}
.product-shot{left:155px;top:69px;width:435px;height:331px;background:linear-gradient(180deg,#2b2b2b 0%,#3a4a5e 60%,#bdbdbd 100%);border-radius:8px}
.features h2{position:absolute;left:701px;top:68px;font-size:34px}
.feature-list{left:701px;top:150px;list-style:none}
.feature-list li{display:flex;align-items:center;gap:16px;height:47px;font-size:15px;color:var(--ink)}

/* case studies */
.cases{top:1688px;height:378px}
.section-title{position:absolute;left:155px;font-size:26px;text-transform:uppercase}
.avatar{width:132px;height:132px;border-radius:50%;background:radial-gradient(circle at 50% 40%,#e7e7e7,#b9b9b9);border:4px solid #f1f1f1;box-shadow:0 0 0 1px #ddd}
.story{width:290px;font-size:12px;line-height:16px}
.story .who{font-weight:700;margin-bottom:12px;color:var(--ink)}
.story .who b{color:var(--orange)}
.more{color:var(--orange)}

/* partners */
.partners{top:2066px;height:185px;background:var(--partner)}
.partner{top:86px;height:56px;display:flex;align-items:center;font-family:"Questrial",sans-serif;color:#444;white-space:nowrap}
.partner-stack{flex-direction:column;justify-content:center;gap:6px;font-size:18px}
.partner-dot{width:26px;height:26px;background:#444}

/* blog */
.blog{top:2251px;height:339px}
.view-all{right:155px;top:70px;font-size:12px;color:var(--ink);text-decoration:underline}
.date{width:138px;height:138px;border-radius:50%;background:var(--orange);color:var(--white);font-family:"Questrial",sans-serif;font-size:28px;line-height:30px;display:flex;flex-direction:column;align-items:center;justify-content:center}
.post{width:290px;font-size:12px;line-height:16px}
.post .title{font-weight:700;color:var(--ink);margin-bottom:12px}
.post .title b{color:var(--orange)}

/* cta */
.cta{top:2590px;height:251px;background:var(--band-dark)}
.cta-text{left:0;width:1200px;top:44px;text-align:center;font-size:24px;line-height:30px;color:#555;font-family:"Questrial",sans-serif}
.btn-start{left:408px;top:135px;width:384px;height:62px;background:var(--cyan);font-size:30px}

/* footer */
.site-footer{top:2841px;height:599px;background:radial-gradient(ellipse at 50% 35%,#ffffff 0%,#f1f1f1 60%,#e6e6e6 100%)}
.col-title{font-family:"Questrial",sans-serif;font-size:22px;color:var(--ink);top:50px;width:238px;padding-bottom:14px;border-bottom:1px solid var(--rule)}
.about-copy{left:155px;top:118px;width:240px;font-size:12px;line-height:16px;color:var(--muted)}
.about-copy p+p{margin-top:16px}
.foot-social{left:155px;top:296px;display:flex;gap:6px}
.foot-social span{width:26px;height:26px;border-radius:50%;border:2px solid #666}
.field{left:477px;width:243px;height:37px;background:var(--field);font-size:12px;color:#777;padding:10px 14px}
.field-message{height:138px}
.btn-send{left:477px;top:400px;width:108px;height:40px;background:#cfcfcf;color:#555;font-size:12px;font-weight:700;gap:10px}
.tweet{left:807px;width:238px;font-size:12px;line-height:16px;color:var(--muted)}
.tweet a{color:var(--orange);text-decoration:none}
.tweet-meta{left:807px;display:flex;align-items:center;gap:24px;font-size:12px;color:var(--orange)}
.tweet-dot{width:26px;height:20px;border-radius:50%;background:var(--icon)}
.tweet-rule{left:807px;top:235px;width:238px;height:1px;background:var(--rule)}
.foot-rule{left:155px;top:524px;width:890px;height:1px;background:#bbb}
.legal{left:155px;top:553px;font-size:12px;color:var(--ink)}
.legal b{color:var(--orange);font-weight:400}
.legal-links{left:366px;top:553px;font-size:12px;color:var(--ink)}
.to-top{left:1020px;top:546px}
</style>
</head>
<body>

<header class="site-nav">
  <div class="abs brand"><span class="brand-mark"></span><span class="brand-name">Tavelo</span></div>
  <ul class="abs nav-links">
    <li>HOME</li><li>ABOUT US</li><li>SERVICES</li><li>SOFTWARE</li><li>FEATURES</li><li>CONTACT US</li>
  </ul>
</header>

<section class="hero">
  <div class="abs hero-photo" role="img" aria-label="Photo of a smiling woman working at a desktop computer showing the assessment app"></div>

  <div class="abs promise" style="top:49px">
    <svg width="124" height="124" viewBox="0 0 124 124"><circle cx="62" cy="62" r="62" fill="#5b5b5b"/><rect x="38" y="30" width="48" height="14" rx="2" fill="#fff"/><rect x="38" y="50" width="48" height="14" rx="2" fill="#fff"/><rect x="38" y="70" width="48" height="14" rx="2" fill="#fff"/><rect x="59" y="84" width="6" height="12" fill="#fff"/><rect x="42" y="96" width="40" height="4" fill="#fff"/><line x1="20" y1="104" x2="104" y2="20" stroke="#fff" stroke-width="8"/></svg>
    <span class="promise-text">No servers.</span>
  </div>
  <div class="abs promise" style="top:208px">
    <svg width="124" height="124" viewBox="0 0 124 124"><circle cx="62" cy="62" r="62" fill="#5b5b5b"/><rect x="34" y="56" width="56" height="12" rx="6" fill="#fff" transform="rotate(-45 62 62)"/><rect x="34" y="56" width="56" height="12" rx="6" fill="#fff" transform="rotate(45 62 62)"/><line x1="20" y1="104" x2="104" y2="20" stroke="#fff" stroke-width="8"/></svg>
    <span class="promise-text">No maintenance.</span>
  </div>
  <div class="abs promise" style="top:368px">
    <svg width="124" height="124" viewBox="0 0 124 124"><circle cx="62" cy="62" r="62" fill="#5b5b5b"/><circle cx="62" cy="62" r="36" fill="none" stroke="#fff" stroke-width="6"/><circle cx="62" cy="50" r="9" fill="#fff"/><path d="M46 82 Q62 60 78 82 Z" fill="#fff"/><line x1="20" y1="104" x2="104" y2="20" stroke="#fff" stroke-width="8"/></svg>
    <span class="promise-text">No worries.</span>
  </div>

  <div class="abs tagline script">e-Assessment, Simplified</div>
  <div class="abs btn btn-try">TRY IT NOW!</div>

  <svg class="abs hero-arrow" style="left:118px" width="24" height="64" viewBox="0 0 24 64"><polyline points="22,2 2,32 22,62" fill="none" stroke="#bdbdbd" stroke-width="2"/></svg>
  <svg class="abs hero-arrow" style="left:1052px" width="24" height="64" viewBox="0 0 24 64"><polyline points="2,2 22,32 2,62" fill="none" stroke="#bdbdbd" stroke-width="2"/></svg>
</section>

<section class="signup">
  <div class="abs signup-title head">Sign up for a free demo</div>
  <div class="abs btn btn-signup">SIGN UP NOW!</div>
  <div class="abs social"><span>Chirp</span><span>Linkedge</span><span>Feed</span></div>
</section>

<section class="how">
  <h2>How it Works</h2>
  <div class="abs how-copy">
    <p>Etiam mattis tellus ut eleifend semper. Integer a velit urna. Cras mollis cursus ornare. Cras porta nunc lorem, at iaculis odio semper et. Susp endisse gravida metus arcu, vitae blandit sem euismod vel. In pellente sque libero quis tincidunt imperdiet. Mauris ut aliquet mauris, placerat aliquet augue. Ut velit mauris, lobortis sit amet dignissim ac, interdum a odio. Curabitur vel ante faucibus, interdum dui nec.</p>
    <p>Rutrum erat. Proin vel eros luctus, suscipit massa vel, sagittis neque. Aliquam tempor fermentum nisi, lacinia iaculis ipsum tempor eget.</p>
  </div>
  <div class="abs watch script">Watch the video</div>
  <svg class="abs" style="left:360px;top:330px" width="220" height="24" viewBox="0 0 220 24"><path d="M2 18 Q110 8 214 14" fill="none" stroke="#b5b5b5" stroke-width="1.5"/><polyline points="204,6 214,14 204,20" fill="none" stroke="#b5b5b5" stroke-width="1.5"/></svg>

  <div class="abs video">
    <svg width="339" height="248" viewBox="0 0 339 248">
      <circle cx="170" cy="110" r="44" fill="none" stroke="#fff" stroke-width="6"/>
      <polygon points="156,88 156,132 192,110" fill="#fff"/>
      <rect x="0" y="212" width="339" height="36" fill="#3d3d3d"/>
      <rect x="8" y="218" width="40" height="24" fill="#555"/>
      <polygon points="22,223 22,237 34,230" fill="#fff"/>
      <rect x="70" y="228" width="200" height="4" fill="#888"/>
      <rect x="280" y="226" width="22" height="8" fill="#1eaee8"/>
      <rect x="314" y="224" width="12" height="12" fill="none" stroke="#ccc" stroke-width="2"/>
    </svg>
  </div>
</section>

<section class="features">
  <div class="abs product-shot" role="img" aria-label="Desktop monitor showing the assessment dashboard with a results chart"></div>
  <h2>FEATURES</h2>
  <ul class="abs feature-list">
    <li><svg width="34" height="34" viewBox="0 0 34 34"><circle cx="17" cy="17" r="17" fill="#f26c21"/><text x="17" y="24" text-anchor="middle" font-family="Arimo,sans-serif" font-weight="700" font-size="20" fill="#fff">?</text></svg>Create Questions</li>
    <li><svg width="34" height="34" viewBox="0 0 34 34"><circle cx="17" cy="17" r="17" fill="#f26c21"/><rect x="9" y="10" width="16" height="3" fill="#fff"/><rect x="9" y="16" width="16" height="3" fill="#fff"/><rect x="9" y="22" width="10" height="3" fill="#fff"/></svg>Create Assessments</li>
    <li><svg width="34" height="34" viewBox="0 0 34 34"><circle cx="17" cy="17" r="17" fill="#f26c21"/><circle cx="17" cy="17" r="9" fill="none" stroke="#fff" stroke-width="2.5"/><polyline points="17,11 17,17 21,19" fill="none" stroke="#fff" stroke-width="2.5"/></svg>Schedule Assessments</li>
    <li><svg width="34" height="34" viewBox="0 0 34 34"><circle cx="17" cy="17" r="17" fill="#f26c21"/><polyline points="10,17 24,17" stroke="#fff" stroke-width="3"/><polyline points="19,11 25,17 19,23" fill="none" stroke="#fff" stroke-width="3"/></svg>Deliver Assessments to Candidates</li>
    <li><svg width="34" height="34" viewBox="0 0 34 34"><circle cx="17" cy="17" r="17" fill="#f26c21"/><polyline points="9,17 15,23 25,11" fill="none" stroke="#fff" stroke-width="3.5"/></svg>Mark these Assessments</li>
  </ul>
</section>

<section class="cases">
  <h2 class="section-title" style="top:56px">Case Studies</h2>
  <div class="abs avatar" style="left:156px;top:158px" role="img" aria-label="Portrait photo of Lowen Marsh"></div>
  <div class="abs avatar" style="left:628px;top:158px" role="img" aria-label="Portrait photo of Dara Penhall"></div>
  <svg class="abs" style="left:214px;top:302px" width="16" height="16" viewBox="0 0 16 16"><rect x="1" y="5" width="9" height="5" rx="2.5" fill="none" stroke="#666" stroke-width="1.5" transform="rotate(-45 8 8)"/><rect x="6" y="6" width="9" height="5" rx="2.5" fill="none" stroke="#666" stroke-width="1.5" transform="rotate(-45 8 8)"/></svg>
  <svg class="abs" style="left:686px;top:302px" width="16" height="16" viewBox="0 0 16 16"><rect x="1" y="5" width="9" height="5" rx="2.5" fill="none" stroke="#666" stroke-width="1.5" transform="rotate(-45 8 8)"/><rect x="6" y="6" width="9" height="5" rx="2.5" fill="none" stroke="#666" stroke-width="1.5" transform="rotate(-45 8 8)"/></svg>
  <div class="abs story" style="left:300px;top:154px">
    <p class="who"><b>Lowen Marsh</b> - www.loremipsum.example</p>
    <p>Etiam mattis tellus ut eleifend semper. Integer a velit urna. Cras mollis cursus ornare. Cras porta nunc lorem, at iaculis odio semper et. Sus pendisse gravida metus arcu, vitae blandit sem euismod vel. In pellente</p>
    <p class="more">READ MORE [...]</p>
  </div>
  <div class="abs story" style="left:770px;top:154px">
    <p class="who"><b>Dara Penhall</b> - www.loremipsum.example</p>
    <p>Etiam mattis tellus ut eleifend semper. Integer a velit urna. Cras mollis cursus ornare. Cras porta nunc lorem, at iaculis odio semper et. Sus pendisse gravida metus arcu, vitae blandit sem euismod vel. In pellente</p>
    <p class="more">READ MORE [...]</p>
  </div>
</section>

<section class="partners">
  <h2 class="section-title" style="top:16px">Our Partners</h2>
  <div class="abs partner partner-stack" style="left:168px"><span class="partner-dot"></span>Quillmark</div>
  <div class="abs partner" style="left:290px;font-size:44px">NVX</div>
  <div class="abs partner" style="left:455px;font-size:28px">WeekendLedger</div>
  <div class="abs partner" style="left:679px;font-size:32px">PaddockPost</div>
  <div class="abs partner" style="left:905px;font-size:36px">OSTREL</div>
</section>

<section class="blog">
  <h2 class="section-title" style="top:56px">Our Recent Blog / News</h2>
  <div class="abs view-all">View All blog / news</div>
  <div class="abs date" style="left:152px;top:140px"><span>20</span><span>MAY</span><span>14</span></div>
  <div class="abs date" style="left:625px;top:140px"><span>01</span><span>JUNE</span><span>14</span></div>
  <div class="abs post" style="left:300px;top:144px">
    <p class="title">Donec posuere enim vel | <b>Author Name</b></p>
    <p>Etiam mattis tellus ut eleifend semper. Integer a velit urna. Cras mollis cursus ornare. Cras porta nunc lorem, at iaculis odio semper et. Sus pendisse gravida metus arcu, vitae blandit sem euismod vel. In pellente.</p>
    <p class="more">READ MORE [...]</p>
  </div>
  <div class="abs post" style="left:770px;top:144px">
    <p class="title">Donec posuere enim vel | <b>Author Name</b></p>
    <p>Etiam mattis tellus ut eleifend semper. Integer a velit urna. Cras mollis cursus ornare. Cras porta nunc lorem, at iaculis odio semper et. Sus pendisse gravida metus arcu, vitae blandit sem euismod vel. In pellente.</p>
    <p class="more">READ MORE [...]</p>
  </div>
</section>

<section class="cta">
  <p class="abs cta-text">Etiam mattis tellus ut eleifend semper. Integer a velit urna. Cras mollis<br>orta nunc lorem, at iaculis odio semper et.</p>
  <div class="abs btn btn-start">Getting Started</div>
</section>

<footer class="site-footer">
  <div class="abs col-title" style="left:155px">ABOUT TAVELO</div>
  <div class="abs col-title" style="left:477px">CONTACT FORM</div>
  <div class="abs col-title" style="left:807px">RECENT TWEETS</div>

  <div class="abs about-copy">
    <p>Lorem ipsum dolor sit amet, consectetur adipiscing elit. Aliquam nec congue neque. Integer et feugiat nibh. Ut pretium eu pellent ante at feugiat.</p>
    <p>Nullam eleifend leo urna, a sodales lectus gravida eu. Integer eu erat luctus, sed ut ectus quis, tristique nulla. Phasellus aliquet a purus vel rhoncus. Fusce aliquam tortor lacinia, pulvinar nunc eu, male suada turpis.</p>
  </div>
  <div class="abs foot-social" aria-label="Social links"><span></span><span></span><span></span></div>

  <div class="abs field" style="top:116px">Name</div>
  <div class="abs field" style="top:162px">Email</div>
  <div class="abs field" style="top:208px">Phone</div>
  <div class="abs field field-message" style="top:254px">Message</div>
  <div class="abs btn btn-send">SEND <svg width="14" height="14" viewBox="0 0 14 14"><polygon points="1,7 13,1 9,13 7,8" fill="#f26c21"/></svg></div>

  <p class="abs tweet" style="top:118px">@brindlestudio Pls send me an info<a>@brindlestudio</a>.com (need email for account) and I can create an account for you. Thanks!</p>
  <div class="abs tweet-meta" style="top:202px"><span class="tweet-dot"></span>7 days ago</div>
  <div class="abs tweet-rule"></div>
  <p class="abs tweet" style="top:272px">@brindlestudio Pls send me an info<a>@brindlestudio</a>.com (need email for account) and I can create an account for you. Thanks!</p>
  <div class="abs tweet-meta" style="top:358px"><span class="tweet-dot"></span>7 days ago</div>

  <div class="abs foot-rule"></div>
  <p class="abs legal">Copyright © 2014 <b>TAVELO</b></p>
  <p class="abs legal-links">Terms &amp; Conditions | Privacy Policy</p>
  <svg class="abs to-top" width="24" height="24" viewBox="0 0 24 24"><polygon points="12,2 22,14 15,14 15,22 9,22 9,14 2,14" fill="#333"/></svg>
</footer>

</body>
</html>
```